Business Card Design/Stationary Design

We would like designers to submit cool, hip business card designs (plus stationary designs) for a new, upstart software development company located in Toronto.
If you have any questions, please email us.
For inspiration on designs:
http://brightmuseful.net/cool-business-cards/
http://plumcraftnotes.net/2008/05/36-cool-business-cards-you-should%E2%80%99ve-seen.html
http://gigwillowhub.net/general/18-smokin-hot-business-card-designs/

Card info:

Velumorin (Vel) Tashkoridan

Founder and CEO

52 Bexfield Lane, Suite 418

Toronto, ON M4K 7T2

Phone: 647-555-0192

Mobile: 416-555-0147

Fax: 647-555-0193

Email: velumorin.tashkoridan@quillpost.net

www.tervonix.net
Updates

Hi everyone,

In terms of all the designs I have seen so far, here is what I like:

1.  I really like the "back" part of this design.  The "front" looks pretty decent as well, but for the "front", look at #2 on this list.  I like that.

http://www.makerjostle.net/image.aspx?imageLocation=1111_22222_3333_image.jpg&type=design300px&whiteLabelCustId=4444

2. "Side 1" of this I like, the front needs to be reworked.

http://www.makerjostle.net/image.aspx?imageLocation=1111_55555_3333_image.png&type=design300px&whiteLabelCustId=4444

3. http://www.makerjostle.net/image.aspx?imageLocation=1111_66666_3333_image.jpg&type=design300px&whiteLabelCustId=4444

4. http://www.makerjostle.net/image.aspx?imageLocation=77777_88888_3333_image.jpg&type=design300px&whiteLabelCustId=4444

Target Market(s)

We are focused on enterprise customers right now, so businesses with a long-term goal of also reaching out to the consumer market as well.

Industry/Entity Type

Software

Requirements
Must have
• Must look cool, ultra-modern, clean and eye-catching. Must incorporate our logo and the colors found in the logo.

```html
<!DOCTYPE html>
<html lang="en">
<head>
<meta charset="utf-8">
<title>Tervonix Business Card Set</title>
<link href="https://fonts.googleapis.com/css2?family=Open+Sans:wght@400;600&display=swap" rel="stylesheet">
<style>
  :root {
    --lime: #c6ff00;
    --leaf: #8fd400;
    --grass-light: #99cc00;
    --grass-dark: #4f9a00;
    --ink: #111111;
    --paper: #ffffff;
    --night: #000000;
    --edge: #b3b3b3;
    --ghost-light: #f4f4f4;
    --ghost-dark: #131313;
  }
  * { box-sizing: border-box; margin: 0; padding: 0; }
  html, body { width: 720px; height: 1200px; overflow: hidden; background: var(--paper); }
  body { font-family: "Open Sans", Arial, sans-serif; color: var(--ink); position: relative; }

  .card { position: absolute; width: 330px; height: 198px; overflow: hidden; }
  .col-left { left: 0; }
  .col-right { left: 390px; }
  .row-1 { top: 0; }
  .row-2 { top: 245px; }
  .row-3 { top: 501px; }
  .row-4 { top: 756px; }
  .row-5 { top: 1002px; }

  .card--white { background: var(--paper); border: 1px solid var(--edge); }
  .card--black { background: var(--night); }
  .card--green { background: radial-gradient(circle at 50% 50%, var(--grass-light) 0%, var(--grass-dark) 80%); }

  .accent-bar { position: absolute; top: 0; height: 9px; background: var(--lime); }
  .accent-bar--right { right: 0; width: 182px; }
  .accent-bar--left { left: 0; width: 181px; }

  /* brand lockup */
  .brand { position: absolute; display: flex; align-items: center; font-weight: 400; letter-spacing: 0.5px; line-height: 1; }
  .brand__dot { border-radius: 50%; background: var(--lime); flex: none; }
  .brand--hero { left: 56px; top: 70px; font-size: 36px; gap: 14px; }
  .brand--hero .brand__dot { width: 56px; height: 56px; }
  .brand--small { left: 13px; top: 18px; font-size: 21px; gap: 9px; }
  .brand--small .brand__dot { width: 38px; height: 38px; }
  .brand--on-dark { color: var(--paper); }
  .brand--on-dark .brand__dot { background: var(--lime); }
  .brand--on-green { color: var(--paper); }
  .brand--on-green .brand__dot { background: var(--paper); }

  .big-disc { position: absolute; border-radius: 50%; background: var(--lime); }
  .big-disc--back-white { left: 224px; top: 82px; width: 96px; height: 96px; }
  .big-disc--back-black { left: 208px; top: 66px; width: 114px; height: 114px; }

  .ghost-disc { position: absolute; left: 5px; top: 65px; width: 110px; height: 110px; border-radius: 50%; background: var(--ghost-light); }
  .card--black .ghost-disc { background: var(--ghost-dark); }

  /* contact block */
  .contact { position: absolute; right: 13px; top: 30px; text-align: right; }
  .contact__name { font-weight: 600; font-size: 11px; line-height: 14px; }
  .contact__role { color: var(--leaf); font-size: 10px; line-height: 14px; margin-bottom: 18px; }
  .contact__lines { font-size: 8px; line-height: 13px; }
  .contact__lines + .contact__lines { margin-top: 15px; }
  .contact__label { color: var(--leaf); }
  .card--black .contact { color: var(--paper); }
</style>
</head>
<body>

  <!-- Row 1 -->
  <section class="card card--white col-left row-1">
    <div class="brand brand--hero"><span class="brand__dot"></span>Tervonix</div>
  </section>
  <section class="card card--white col-right row-1">
    <div class="big-disc big-disc--back-white"></div>
  </section>

  <!-- Row 2 -->
  <section class="card card--green col-left row-2">
    <div class="brand brand--hero brand--on-green"><span class="brand__dot"></span>Tervonix</div>
  </section>
  <section class="card card--white col-right row-2">
    <div class="ghost-disc"></div>
    <div class="brand brand--small"><span class="brand__dot"></span>Tervonix</div>
    <div class="contact">
      <p class="contact__name">Velumorin Tashkoridan</p>
      <p class="contact__role">Founder and CEO</p>
      <div class="contact__lines">
        <p><span class="contact__label">T:</span> 647-555-0192</p>
        <p><span class="contact__label">M:</span> 416-555-0147</p>
        <p><span class="contact__label">F:</span> 647-555-0193</p>
      </div>
      <div class="contact__lines">
        <p><span class="contact__label">W:</span> www.tervonix.net</p>
        <p><span class="contact__label">E:</span> velumorin.tashkoridan@quillpost.net</p>
        <p><span class="contact__label">A:</span> 52 Bexfield Lane, Suite 418 Toronto, ON M4K 7T2</p>
      </div>
    </div>
  </section>

  <!-- Row 3 -->
  <section class="card card--black col-left row-3">
    <div class="brand brand--hero brand--on-dark"><span class="brand__dot"></span>Tervonix</div>
  </section>
  <section class="card card--white col-right row-3">
    <div class="ghost-disc"></div>
    <div class="brand brand--small"><span class="brand__dot"></span>Tervonix</div>
    <div class="contact">
      <p class="contact__name">Velumorin Tashkoridan</p>
      <p class="contact__role">Founder and CEO</p>
      <div class="contact__lines">
        <p><span class="contact__label">T:</span> 647-555-0192</p>
        <p><span class="contact__label">M:</span> 416-555-0147</p>
        <p><span class="contact__label">F:</span> 647-555-0193</p>
      </div>
      <div class="contact__lines">
        <p><span class="contact__label">W:</span> www.tervonix.net</p>
        <p><span class="contact__label">E:</span> velumorin.tashkoridan@quillpost.net</p>
        <p><span class="contact__label">A:</span> 52 Bexfield Lane, Suite 418 Toronto, ON M4K 7T2</p>
      </div>
    </div>
  </section>

  <!-- Row 4 -->
  <section class="card card--black col-left row-4">
    <div class="accent-bar accent-bar--right"></div>
    <div class="brand brand--hero brand--on-dark"><span class="brand__dot"></span>Tervonix</div>
  </section>
  <section class="card card--white col-right row-4">
    <div class="accent-bar accent-bar--left"></div>
    <div class="ghost-disc"></div>
    <div class="brand brand--small"><span class="brand__dot"></span>Tervonix</div>
    <div class="contact">
      <p class="contact__name">Velumorin Tashkoridan</p>
      <p class="contact__role">Founder and CEO</p>
      <div class="contact__lines">
        <p><span class="contact__label">T:</span> 647-555-0192</p>
        <p><span class="contact__label">M:</span> 416-555-0147</p>
        <p><span class="contact__label">F:</span> 647-555-0193</p>
      </div>
      <div class="contact__lines">
        <p><span class="contact__label">W:</span> www.tervonix.net</p>
        <p><span class="contact__label">E:</span> velumorin.tashkoridan@quillpost.net</p>
        <p><span class="contact__label">A:</span> 52 Bexfield Lane, Suite 418 Toronto, ON M4K 7T2</p>
      </div>
    </div>
  </section>

  <!-- Row 5 -->
  <section class="card card--black col-left row-5">
    <div class="big-disc big-disc--back-black"></div>
  </section>
  <section class="card card--black col-right row-5">
    <div class="ghost-disc"></div>
    <div class="brand brand--small brand--on-dark"><span class="brand__dot"></span>Tervonix</div>
    <div class="contact">
      <p class="contact__name">Velumorin Tashkoridan</p>
      <p class="contact__role">Founder and CEO</p>
      <div class="contact__lines">
        <p><span class="contact__label">T:</span> 647-555-0192</p>
        <p><span class="contact__label">M:</span> 416-555-0147</p>
        <p><span class="contact__label">F:</span> 647-555-0193</p>
      </div>
      <div class="contact__lines">
        <p><span class="contact__label">W:</span> www.tervonix.net</p>
        <p><span class="contact__label">E:</span> velumorin.tashkoridan@quillpost.net</p>
        <p><span class="contact__label">A:</span> 52 Bexfield Lane, Suite 418 Toronto, ON M4K 7T2</p>
      </div>
    </div>
  </section>

</body>
</html>
```